Brochure for a six month Life Transformation program for executives

I need a A4 brochure that will be physically printed out to give to prospective clients for a six month coaching, life transformation program. I have included here a video link that discusses the brief in detail.
https://www.vidtrellis.com/share/4b81e2f09c3d47a6b52e18d0a7f3c915

I've uploaded a file with logos and photos to include as well as a outline of each page.
Updates

Here is an updated video to show you what I'm liking what I don't like https://www.vidtrellis.com/share/e92d07b1a6f84c3098d5b7c1f4a26e08

Target Market(s)

35 - 55 male executives

Industry/Entity Type

Life Coaching

Requirements
Must have
• All the information in the outline
Nice to have
• icons, vector diagrams, the theme of transformation and revolution

```html
<!DOCTYPE html>
<html lang="en">
<head>
<meta charset="utf-8">
<title>Northpeak Renewal – Brochure Cover</title>
<link href="https://fonts.googleapis.com/css2?family=Open+Sans:wght@400;600&display=swap" rel="stylesheet">
<style>
  :root {
    --navy: #0b3d8f;
    --royal: #1f64c4;
    --sky: #9ec1ec;
    --paper: #ffffff;
    --ink: #3c3f44;
    --backdrop: #e6e8eb;
  }
  html, body {
    margin: 0;
    padding: 0;
    width: 1177px;
    height: 1200px;
    overflow: hidden;
    background: var(--backdrop);
    font-family: "Open Sans", Arial, sans-serif;
  }
  .canvas {
    position: relative;
    width: 1177px;
    height: 1200px;
  }
  .cover {
    position: absolute;
    left: 185px;
    top: 30px;
    width: 806px;
    height: 1140px;
    background: var(--paper);
    box-shadow: 0 6px 24px rgba(0,0,0,0.18);
    overflow: hidden;
  }
  .cover-art {
    position: absolute;
    inset: 0;
    width: 806px;
    height: 1140px;
  }
  .brand {
    position: absolute;
    left: 90px;
    top: 196px;
    margin: 0;
    font-size: 27px;
    font-weight: 600;
    letter-spacing: 5px;
    text-transform: uppercase;
    color: var(--navy);
    display: flex;
    align-items: center;
    gap: 14px;
  }
  .brand-mark {
    width: 18px;
    height: 18px;
    background: var(--navy);
  }
  .headline {
    position: absolute;
    right: 48px;
    top: 330px;
    margin: 0;
    text-align: right;
    list-style: none;
    padding: 0;
  }
  .headline li {
    font-size: 38px;
    font-weight: 400;
    color: var(--navy);
    padding-bottom: 6px;
    margin-bottom: 22px;
    border-bottom: 2px solid var(--sky);
    line-height: 1.1;
  }
  .summary {
    position: absolute;
    right: 48px;
    top: 600px;
    width: 270px;
    margin: 0;
    text-align: right;
    font-size: 18px;
    line-height: 1.6;
    color: var(--ink);
  }
  .summary .accent {
    color: var(--royal);
    font-weight: 600;
  }
</style>
</head>
<body>
<div class="canvas">
  <article class="cover">
    <svg class="cover-art" viewBox="0 0 806 1140" xmlns="http://www.w3.org/2000/svg">
      <defs>
        <linearGradient id="stripe" x1="0" y1="0" x2="1" y2="0">
          <stop offset="0" stop-color="#dbe7f7"/>
          <stop offset="0.5" stop-color="#8fb4e6"/>
          <stop offset="1" stop-color="#1f64c4"/>
        </linearGradient>
        <linearGradient id="scene" x1="0" y1="0" x2="0" y2="1">
          <stop offset="0" stop-color="#dfe9f1"/>
          <stop offset="0.45" stop-color="#c6d8e4"/>
          <stop offset="0.7" stop-color="#c9c2b8"/>
          <stop offset="1" stop-color="#b5ada3"/>
        </linearGradient>
        <linearGradient id="fade" x1="0" y1="0" x2="1" y2="0">
          <stop offset="0.45" stop-color="#ffffff" stop-opacity="0"/>
          <stop offset="0.72" stop-color="#ffffff" stop-opacity="0.9"/>
          <stop offset="1" stop-color="#ffffff" stop-opacity="1"/>
        </linearGradient>
      </defs>
      <!-- top corner block -->
      <polygon class="block-top" points="300,0 806,0 806,180 610,238" fill="var(--navy)"/>
      <!-- left accent -->
      <polygon class="block-left" points="0,330 190,385 0,440" fill="var(--navy)"/>
      <!-- upper stripe -->
      <polygon points="0,440 806,185 806,207 0,462" fill="url(#stripe)"/>
      <!-- feature photo area -->
      <g role="img" aria-label="Photo of a woman in running gear crouched in a sprint start on a seaside path">
        <polygon points="0,478 806,222 806,840 0,1075" fill="url(#scene)"/>
        <polygon points="0,478 806,222 806,840 0,1075" fill="url(#fade)"/>
      </g>
      <!-- lower stripe -->
      <polygon points="0,1080 806,846 806,868 0,1102" fill="url(#stripe)"/>
      <!-- bottom corner block -->
      <polygon class="block-bottom" points="430,1140 806,1140 806,930 640,978" fill="var(--navy)"/>
    </svg>

    <h1 class="brand"><span class="brand-mark"></span>Northpeak Renewal</h1>

    <ul class="headline">
      <li>Your Life</li>
      <li>Your Potential</li>
      <li>Your Revolution</li>
    </ul>

    <p class="summary">A six month <span class="accent">life transformation</span> program for overworked executives to restore life balance through health and fitness optimization while maintaining their high functioning career.</p>
  </article>
</div>
</body>
</html>
```